Business Card Design

Hoping for a black background business card, minimalistic design.
With the Marble Crest logo you created in white.

I would like to include:
My Name and title
Address (street address)
Reception: (phone number)
Fax: (fax number)
Reception: (email address)
Direct email: (email address)
Instagram: (ig handle)

```html
<!DOCTYPE html>
<html lang="en">
<head>
<meta charset="utf-8">
<title>Marble Crest – Business Card</title>
<link href="https://fonts.googleapis.com/css2?family=Open+Sans:wght@400;600;700&display=swap" rel="stylesheet">
<style>
  :root{
    --stage:#2b2b2e;
    --card-dark:#1f1f23;
    --emboss:#2c2c31;
    --white:#ffffff;
    --ink:#1f1f23;
  }
  *{margin:0;padding:0;box-sizing:border-box}
  html,body{width:1200px;height:780px;overflow:hidden;background:var(--stage);font-family:"Open Sans",sans-serif}
  .stage{position:relative;width:1200px;height:780px;display:flex;gap:40px;align-items:center;justify-content:center}
  .card{position:relative;width:540px;height:309px;background:var(--card-dark);overflow:hidden;box-shadow:0 18px 40px rgba(0,0,0,.45)}

  /* front */
  .front-mark{position:absolute;left:0;top:0;width:100%;height:100%;display:flex;align-items:center;justify-content:center;gap:18px}
  .front-mark .dot{width:70px;height:70px;border-radius:50%;border:3px solid var(--emboss)}
  .front-mark .rule{width:1px;height:74px;background:var(--emboss)}
  .front-mark .wordmark{font-weight:600;font-size:34px;letter-spacing:4px;color:var(--emboss);text-transform:uppercase}

  /* back */
  .back .white-field{position:absolute;left:0;top:178px;width:100%;height:131px;background:var(--white)}
  .back .seal{position:absolute;left:372px;top:105px;width:168px;height:168px;border-radius:50%;background:var(--card-dark);border:7px solid var(--white);box-shadow:0 0 0 5px var(--card-dark), 0 0 0 8px var(--white)}
  .name-block{position:absolute;right:34px;top:18px;text-align:right;color:var(--white)}
  .name-block .person{font-weight:700;font-size:27px;line-height:1.1}
  .name-block .role{font-size:14px;letter-spacing:.5px}
  .name-tab{position:absolute;right:0;top:20px;width:20px;height:36px;background:var(--white)}
  .brand-row{position:absolute;left:26px;top:104px;display:flex;align-items:center;gap:10px}
  .brand-row .dot{width:44px;height:44px;border-radius:50%;border:3px solid var(--white)}
  .brand-row .rule{width:1px;height:52px;background:#8a8a8f}
  .brand-row .wordmark{font-weight:600;font-size:23px;letter-spacing:3px;color:var(--white);text-transform:uppercase}
  .contact{position:absolute;left:26px;top:186px;color:var(--ink)}
  .contact .address{font-size:14px;line-height:1.2;margin-bottom:5px}
  .contact ul{list-style:none}
  .contact li{display:flex;align-items:center;gap:8px;font-size:12.5px;line-height:1.35}
  .contact li svg{width:11px;height:11px;flex:none}
  .contact .note{font-size:8.5px;margin-left:2px}
</style>
</head>
<body>
<main class="stage">
  <section class="card front" aria-label="Card front">
    <div class="front-mark">
      <span class="dot"></span>
      <span class="rule"></span>
      <span class="wordmark">Marble Crest</span>
    </div>
  </section>

  <section class="card back" aria-label="Card back">
    <div class="white-field"></div>
    <div class="seal"></div>
    <div class="name-tab"></div>
    <div class="name-block">
      <div class="person">Lena Vorland</div>
      <div class="role">Managing Director</div>
    </div>
    <div class="brand-row">
      <span class="dot"></span>
      <span class="rule"></span>
      <span class="wordmark">Marble Crest</span>
    </div>
    <div class="contact">
      <p class="address">418 Harlow Ave. Suite 300<br>Denton, TX 76201</p>
      <ul>
        <li><svg viewBox="0 0 12 12"><path d="M2.5 1l2 2.2-1 1.3a7 7 0 0 0 4 4l1.3-1 2.2 2-1.3 1.5C5.5 11 1 6.5 1 2.3z" fill="var(--ink)"/></svg>(555) 214-3086</li>
        <li><svg viewBox="0 0 12 12"><rect x="1" y="4" width="10" height="7" fill="var(--ink)"/><rect x="3" y="1" width="6" height="3" fill="none" stroke="var(--ink)"/></svg>(555) 214-3099</li>
        <li><svg viewBox="0 0 12 12"><rect x="1.5" y="1.5" width="9" height="9" fill="none" stroke="var(--ink)" stroke-width="1.5"/></svg>@website.com</li>
        <li><svg viewBox="0 0 12 12"><rect x="1" y="2.5" width="10" height="7" fill="none" stroke="var(--ink)"/><path d="M1 2.5l5 4 5-4" fill="none" stroke="var(--ink)"/></svg>info@website.com<span class="note">(Reception)</span></li>
        <li><svg viewBox="0 0 12 12"><rect x="1" y="2.5" width="10" height="7" fill="none" stroke="var(--ink)"/><path d="M1 2.5l5 4 5-4" fill="none" stroke="var(--ink)"/></svg>info@website.com<span class="note">(Direct email)</span></li>
      </ul>
    </div>
  </section>
</main>
</body>
</html>
```